A4 fitness centre email specials brochure

Kelburn Signal Works have been providing audio visual services and support to fitness centres and health clubs for more than 10 years. We are seen as the "to-go" company for anything to do with Audio visual equipment yet we do not produce marketing material or promotional material for these customers so this is our first attempt at promotion. We wish to produce a PDF brochure suitable for emailing to existing and new clients promoting our products and services with special offers using the text contact on the attached draft. The brochure is simple but should carry the company logo in a prominant position, our corporate blue colour, and be easily read. a good photo can be used as a shaded backgound.

Target Market(s)

Health Club managers, fitness instructors

Industry/Entity Type

Fitness Equipment

Font styles to use
Sans Serif

Colors
0455a3

Requirements
Must have
• our corporate colour (blue) a good tag headline (Eg- AV fitness specials) and be easy to read. The brochure will be used as a PDF flyer to attach to emails and may also be printed to mail in some cased
Nice to have
• a picture of a gym with AV equipment in the background, maybe as a water mark image or faded. The brochure should reflect the fitness industry in order to grasp attention to our audience If space allows, maybe just have our offices mentioned in the contact details such as.... Melbourne-Brisbane-Sydney-Perth
Should not have
• don't want it to look cheap - we are the market leader for this sector for over 10 years and it should look professional

```html
<!DOCTYPE html>
<html lang="en">
<head>
<meta charset="utf-8">
<title>Kelburn Signal Works – AV fitness specials</title>
<link href="https://fonts.googleapis.com/css2?family=Source+Sans+3:ital,wght@0,400;0,600;0,700;1,400;1,600;1,700&display=swap" rel="stylesheet">
<style>
  :root {
    --corporate-blue: #0455a3;
    --heading-blue: #1a6fc0;
    --ink: #1d1d1f;
    --rule: #2b2b2b;
    --white: #ffffff;
    --photo-warm: #c9b9a6;
    --photo-cool: #a9c2d4;
    --gear-dark: #3a3a3e;
    --mark-teal: #2a8fbf;
  }
  * { box-sizing: border-box; margin: 0; padding: 0; }
  html, body { width: 848px; height: 1200px; overflow: hidden; background: var(--white); }
  body { font-family: "Source Sans 3", "Helvetica Neue", Arial, sans-serif; color: var(--ink); }
  .brochure { position: relative; width: 848px; height: 1200px; overflow: hidden; }

  .top-band { position: absolute; left: 0; top: 0; width: 848px; height: 17px; background: var(--corporate-blue); }

  .intro { position: absolute; left: 22px; top: 22px; width: 760px; font-size: 21px; line-height: 27px; }
  .intro .company { font-weight: 700; font-style: italic; }

  .section-label { position: absolute; left: 22px; top: 138px; font-size: 22px; font-weight: 700; }
  .section-rule { position: absolute; left: 0; top: 166px; width: 152px; height: 1.5px; background: var(--rule); }

  .service-group { position: absolute; }
  .service-group h2 { color: var(--heading-blue); font-size: 22px; font-weight: 700; margin-bottom: 6px; }
  .service-group ul { list-style: none; }
  .service-group li { position: relative; padding-left: 10px; font-size: 17.5px; line-height: 22px; margin-bottom: 7px; }
  .service-group li::before { content: ""; position: absolute; left: 0; top: 9px; width: 5px; height: 5px; border-radius: 50%; background: var(--corporate-blue); }
  .service-group li.small { font-size: 15.5px; }

  .group-control { left: 20px; top: 172px; width: 460px; }
  .group-audio { left: 20px; top: 374px; width: 500px; }
  .group-visual { left: 480px; top: 166px; width: 360px; }

  .equipment-photo { position: absolute; left: 513px; top: 456px; width: 310px; height: 164px; border-radius: 6px;
    background: linear-gradient(90deg, var(--gear-dark) 0 18%, #e8e8ea 18% 82%, var(--gear-dark) 82%); opacity: .9; }

  .reseller-note { position: absolute; left: 12px; top: 640px; width: 820px; font-size: 17.5px; line-height: 22px; font-style: italic; }

  .gym-photo { position: absolute; left: 0; top: 695px; width: 848px; height: 296px;
    background: linear-gradient(180deg, #eef3f6 0%, var(--photo-cool) 35%, var(--photo-warm) 70%, #6d6a6b 100%); }

  .brand-block { position: absolute; left: 0; top: 1006px; width: 848px; display: flex; justify-content: center; align-items: center; gap: 22px; }
  .brand-square { width: 58px; height: 58px; background: var(--mark-teal); }
  .brand-text { display: flex; flex-direction: column; align-items: center; }
  .brand-name { font-size: 46px; font-weight: 600; color: #2a2a2a; line-height: 52px; letter-spacing: -.5px; }
  .brand-tagline { font-size: 26px; font-style: italic; color: var(--heading-blue); line-height: 30px; }

  .contact-bar { position: absolute; left: 0; top: 1121px; width: 848px; height: 79px; background: var(--corporate-blue);
    display: flex; align-items: center; justify-content: center; gap: 16px; color: var(--white); font-weight: 600; font-size: 21px; }
  .contact-bar .dot { font-size: 14px; }
  .contact-bar .phone { font-size: 30px; font-weight: 700; margin-left: 12px; }
</style>
</head>
<body>
<main class="brochure">
  <div class="top-band"></div>

  <p class="intro"><span class="company">Kelburn Signal Works</span> was established in Melbourne in June of 2000. With offices in Melbourne, Sydney, Brisbane and Perth we provide state based, national and global organisations a complete, consistent and diverse range of audio visual products and services.</p>

  <div class="section-label">What we do:</div>
  <div class="section-rule"></div>

  <section class="service-group group-control">
    <h2>AV Control Systems</h2>
    <ul>
      <li>Commercial Control Integration and Automation</li>
      <li>Control System Software Architecture -<br>(Corvane, Linqora, Tessix)</li>
      <li>Multiple Technology Integration</li>
      <li>Control System Procurement and Design</li>
    </ul>
  </section>

  <section class="service-group group-audio">
    <h2>Audio</h2>
    <ul>
      <li>Paging and Public Address</li>
      <li class="small">Background Music</li>
      <li>Live Entertainment Audio</li>
      <li>Multiroom / Multizone Audio Distribution and Processing</li>
      <li>“Cardio Stage” Entertainment Systems</li>
      <li>Automated Sound Level Control</li>
      <li>Conferencing Systems</li>
    </ul>
  </section>

  <section class="service-group group-visual">
    <h2>Visual</h2>
    <ul>
      <li>Interactive LED/LCD Touch Screens</li>
      <li>Multi-screen Video Walls &amp; Distribution</li>
      <li>Video &amp; Data Projection</li>
      <li class="small">Video Conferencing</li>
      <li>Large Screen Display / Projection Systems</li>
      <li>High Definition Video Distribution</li>
      <li>Digital Signage Solutions</li>
      <li>Controlled Lighting Effects</li>
    </ul>
  </section>

  <div class="equipment-photo" role="img" aria-label="Audio equipment: two portable speakers, a wireless microphone receiver, headset mic and rack amplifiers"></div>

  <p class="reseller-note">Also, as an authorised reseller of over 500 different audio visual product lines, we are able to provide you with the best solution and equipment to meet your needs.</p>

  <div class="gym-photo" role="img" aria-label="Photo of a group spin class riding stationary bikes in a bright gym"></div>

  <div class="brand-block">
    <div class="brand-square"></div>
    <div class="brand-text">
      <div class="brand-name">Kelburn Signal Works</div>
      <div class="brand-tagline">AV fitness specials</div>
    </div>
  </div>

  <footer class="contact-bar">
    <span>hello@kelburnsignal.com.au</span>
    <span class="dot">●</span>
    <span>www.kelburnsignal.com.au</span>
    <span class="dot">●</span>
    <span class="phone">1300 555 214</span>
  </footer>
</main>
</body>
</html>
```